Logo for Childcare
The Little Meadow Study House
Use specific fonts
i am open to fonts
Bright & Fun-filled
Marisol Quenby, M.Ed
Executive Director
317 N 29th Street Philadelphia, PA 19128
mquenby@lmsh-demo.org
www.lmsh-demo.org
I would like a solid color background with the logo

```html
<!DOCTYPE html>
<html lang="en">
<head>
<meta charset="utf-8">
<title>The Little Meadow Study House – Stationery Set</title>
<link href="https://fonts.googleapis.com/css2?family=Quicksand:wght@500;700&family=Open+Sans:wght@400;600&display=swap" rel="stylesheet">
<style>
  :root{
    --bg:#8f8f92;
    --purple:#5a3a9e;
    --purple-light:#8a6cc4;
    --paper:#ffffff;
    --paper-shade:#f2f2f4;
    --ink:#4a4a55;
    --label:#e6e6e8;
  }
  *{box-sizing:border-box;margin:0;padding:0}
  html,body{width:1200px;height:490px;overflow:hidden}
  body{background:var(--bg);position:relative;font-family:"Open Sans",sans-serif;color:var(--ink)}
  .piece{position:absolute;background:var(--paper);box-shadow:0 2px 6px rgba(0,0,0,.25)}
  .label{position:absolute;font:600 6px "Open Sans",sans-serif;color:var(--label);text-align:center;width:100%;top:-10px;left:0}
  .brand{display:flex;align-items:center;gap:4px;font-family:"Quicksand",sans-serif;font-weight:700;color:var(--purple);line-height:1.05}
  .brand-dot{width:12px;height:12px;border-radius:50%;background:var(--purple);flex:none}
  .brand.on-dark{color:var(--paper)}
  .brand.on-dark .brand-dot{background:var(--paper)}
  .wave{position:absolute;left:0;bottom:0;width:100%;display:block}

  /* folder */
  .folder{position:absolute;left:24px;top:56px;width:456px;height:400px}
  .folder-label{top:-10px;left:0;width:456px}
  .folder-cover{position:absolute;left:0;top:0;width:259px;height:324px;background:var(--purple);box-shadow:0 2px 6px rgba(0,0,0,.25)}
  .folder-title{position:absolute;left:54px;top:46px;font-family:"Quicksand",sans-serif;color:var(--paper);line-height:1}
  .folder-title .small{display:block;font-size:13px;font-weight:500}
  .folder-title .big{display:block;font-size:27px;font-weight:700;margin:2px 0}
  .folder-back{position:absolute;left:259px;top:0;width:197px;height:324px;background:var(--paper);overflow:hidden;box-shadow:0 2px 6px rgba(0,0,0,.25)}
  .folder-back .brand{position:absolute;left:20px;top:20px;font-size:12px}
  .folder-pockets{position:absolute;left:0;top:324px;width:456px;height:76px;display:block}
  .pocket-brand{position:absolute;left:130px;top:346px;font-size:8px}
  .pocket-brand .brand-dot{width:8px;height:8px}

  /* business cards */
  .card{width:108px;height:50px;top:96px;overflow:hidden}
  .card-front .brand,.card-dark .brand{position:absolute;left:50%;top:50%;transform:translate(-50%,-50%);font-size:8px;white-space:nowrap}
  .card-front .brand-dot,.card-dark .brand-dot{width:9px;height:9px}
  .card-front{left:492px}
  .card-back{left:619px}
  .card-back .brand{position:absolute;left:6px;top:10px;font-size:5px;gap:2px;white-space:nowrap}
  .card-back .brand-dot{width:5px;height:5px}
  .card-contact{position:absolute;right:5px;top:6px;width:50px;text-align:right;font-size:3.3px;line-height:1.35;color:var(--ink);white-space:nowrap}
  .card-contact strong{display:block;font-family:"Quicksand",sans-serif;font-weight:700;color:var(--purple);font-size:4.4px}
  .card-dark{left:744px;background:var(--purple)}

  /* letterheads */
  .letter{top:168px;width:154px;height:240px;overflow:hidden}
  .letter-fax{left:499px}
  .letter-main{left:667px}
  .letter .brand{position:absolute;left:12px;top:12px;font-size:7px}
  .letter .brand-dot{width:8px;height:8px}
  .letter-address{position:absolute;right:10px;top:14px;font-size:3.4px;line-height:1.4;text-align:right}
  .fax-table{position:absolute;left:12px;top:40px;width:130px;border-collapse:collapse;font-size:3.6px}
  .fax-table td{border:0.5px solid #9c93b6;height:7px;padding:0 2px}
  .fax-table td:first-child{width:30px;color:var(--purple);font-weight:600}
  .fax-checks{position:absolute;left:12px;top:92px;display:flex;gap:7px;font-size:3.4px}
  .fax-checks span::before{content:"";display:inline-block;width:3px;height:3px;border:0.5px solid var(--purple);margin-right:1px;vertical-align:middle}

  /* compliment slip */
  .slip{left:840px;top:173px;width:264px;height:139px;overflow:hidden}
  .slip .brand{position:absolute;left:18px;top:16px;font-size:9px}
  .slip .brand-dot{width:10px;height:10px}
  .slip .letter-address{top:18px;right:16px;font-size:4px}

  /* envelope */
  .envelope{left:840px;top:336px;width:264px;height:132px;overflow:hidden}
  .envelope .flap{position:absolute;left:0;top:0;width:100%;height:100%}
  .envelope .brand{position:absolute;left:50%;top:70px;transform:translateX(-50%);font-size:6px;white-space:nowrap}
  .envelope .brand-dot{width:7px;height:7px}
</style>
</head>
<body>

<!-- Presentation folder -->
<section class="folder">
  <div class="label folder-label">Folder</div>
  <div class="folder-cover">
    <div class="folder-title">
      <span class="small">The</span>
      <span class="big">Little Meadow</span>
      <span class="small">Study House</span>
    </div>
  </div>
  <div class="folder-back">
    <div class="brand"><span class="brand-dot"></span><span>The Little Meadow<br>Study House</span></div>
    <svg class="wave" viewBox="0 0 197 60" height="60" preserveAspectRatio="none">
      <path d="M0 38 C60 20 120 30 197 18 L197 60 L0 60Z" fill="var(--purple-light)"/>
      <path d="M0 46 C60 28 130 40 197 28 L197 60 L0 60Z" fill="var(--purple)"/>
    </svg>
  </div>
  <svg class="folder-pockets" viewBox="0 0 456 76">
    <path d="M0 0 L259 0 L259 76 L18 76 L0 56Z" fill="var(--paper)"/>
    <path d="M259 0 L456 0 L456 56 L438 76 L259 76Z" fill="var(--paper-shade)"/>
  </svg>
  <div class="brand pocket-brand"><span class="brand-dot"></span><span>The Little Meadow<br>Study House</span></div>
</section>

<!-- Business cards -->
<div class="piece card card-front">
  <div class="label">Business Card Front</div>
  <div class="brand"><span class="brand-dot"></span><span>The Little Meadow<br>Study House</span></div>
</div>
<div class="piece card card-back">
  <div class="label">Business Card Back</div>
  <div class="brand"><span class="brand-dot"></span><span>The Little Meadow<br>Study House</span></div>
  <div class="card-contact">
    <strong>Marisol Quenby, M.Ed</strong>
    Executive Director<br>
    317 N 29th Street<br>
    Philadelphia, PA 19128<br>
    mquenby@lmsh-demo.org<br>
    www.lmsh-demo.org
  </div>
  <svg class="wave" viewBox="0 0 108 10" height="10" preserveAspectRatio="none">
    <path d="M0 6 C40 0 70 8 108 2 L108 10 L0 10Z" fill="var(--purple)"/>
  </svg>
</div>
<div class="piece card card-dark">
  <div class="label">Business Card Alt</div>
  <div class="brand on-dark"><span class="brand-dot"></span><span>The Little Meadow<br>Study House</span></div>
</div>

<!-- Fax sheet -->
<div class="piece letter letter-fax">
  <div class="label">Fax Sheet</div>
  <div class="brand"><span class="brand-dot"></span><span>The Little Meadow<br>Study House</span></div>
  <table class="fax-table">
    <tr><td>To</td><td></td></tr>
    <tr><td>From</td><td></td></tr>
    <tr><td>Fax</td><td></td></tr>
    <tr><td>Phone</td><td></td></tr>
    <tr><td>Date</td><td></td></tr>
    <tr><td>Pages</td><td></td></tr>
  </table>
  <div class="fax-checks"><span>Urgent</span><span>Review</span><span>Reply</span><span>Recycle</span></div>
  <svg class="wave" viewBox="0 0 154 24" height="24" preserveAspectRatio="none">
    <path d="M0 14 C50 4 100 16 154 6 L154 24 L0 24Z" fill="var(--purple-light)"/>
    <path d="M0 18 C50 8 100 20 154 10 L154 24 L0 24Z" fill="var(--purple)"/>
  </svg>
</div>

<!-- Letterhead -->
<div class="piece letter letter-main">
  <div class="label">Letterhead</div>
  <div class="brand"><span class="brand-dot"></span><span>The Little Meadow<br>Study House</span></div>
  <div class="letter-address">317 N 29th Street<br>Philadelphia, PA 19128<br>www.lmsh-demo.org</div>
  <svg class="wave" viewBox="0 0 154 24" height="24" preserveAspectRatio="none">
    <path d="M0 14 C50 4 100 16 154 6 L154 24 L0 24Z" fill="var(--purple-light)"/>
    <path d="M0 18 C50 8 100 20 154 10 L154 24 L0 24Z" fill="var(--purple)"/>
  </svg>
</div>

<!-- Compliment slip -->
<div class="piece slip">
  <div class="label">Compliment Slip</div>
  <div class="brand"><span class="brand-dot"></span><span>The Little Meadow<br>Study House</span></div>
  <div class="letter-address">317 N 29th Street Philadelphia, PA 19128<br>mquenby@lmsh-demo.org<br>www.lmsh-demo.org</div>
  <svg class="wave" viewBox="0 0 264 30" height="30" preserveAspectRatio="none">
    <path d="M0 16 C90 2 170 20 264 6 L264 30 L0 30Z" fill="var(--purple-light)"/>
    <path d="M0 21 C90 7 170 25 264 11 L264 30 L0 30Z" fill="var(--purple)"/>
  </svg>
</div>

<!-- Envelope -->
<div class="piece envelope">
  <div class="label">Envelope</div>
  <svg class="flap" viewBox="0 0 264 132" preserveAspectRatio="none">
    <path d="M0 0 L264 0 L264 40 L132 100 L0 40Z" fill="var(--purple)"/>
    <path d="M0 40 L132 100 L264 40" fill="none" stroke="var(--purple-light)" stroke-width="1.5"/>
  </svg>
  <div class="brand on-dark"><span class="brand-dot"></span><span>The Little Meadow Study House</span></div>
</div>

</body>
</html>
```